Flyer für Textilien mit individueller Bestickung oder Bedruckung
Wir waren mit der Designerin hochzufrieden. Alle Änderungen und Wünsche wurden schnell und sehr kompetent bearbeitet. Sind von dem Ergebnis begeistert.
Zielgruppe
Vertrieb von Logobekleidung, wie z.B. Strickwaren, Polo Shirts und T Shirts.
Zielgruppe sind Golfclubs, Proshops, Vereine, Schulen (Schulbekleidung ), Arztpraxen sowie alle Firmen und Institutionen, die Bekleidung mit individueller Bestickung oder Bedruckung benötigen.
Aufgabenstellung
Es soll ein Flyer erstellt werden, der nicht überfrachtet ist und dem Kunden schnelle und transparente Informationen liefert. Es sollen sich möglichst viele Branchen angesprochen fühlen. Auf den grünen Button mit "golf" sollte daher verzichtet werden.
Auf unserer Internetseite www.velmax.de wird deutlich, das es zwei Geschäftsfelder in unserer Firma gibt, Golfshop einerseits und Werbetextilien andererseits. Der gewünschte Flyer soll das Thema Werbetextilien abdecken. Im Datenanhang haben wir einen von uns erstellten Flyer angehängt, der lediglich als Anhaltspunkt gelten soll. Wir begrüssen es sehr wenn der Designer sich von der Vorlage löst. Unser Logo 'velmax artline' steht für das Werbetextil Geschäft und ist gleichzeitig unsere Marke, unter der wir unsere Strickwaren produzieren.
Die Sprache sollte Deutsch sein.

```html
<!DOCTYPE html>
<html lang="de">
<head>
<meta charset="utf-8">
<title>velmax artline – Flyer Werbetextilien</title>
<link href="https://fonts.googleapis.com/css2?family=Lato:wght@400;700;900&display=swap" rel="stylesheet">
<style>
  :root {
    --green: #6cbb2e;
    --green-light: #bfe39a;
    --ink: #1d1d1b;
    --ink-soft: #3a3a38;
    --paper: #ffffff;
    --stage: #e9e9e7;
  }
  * { box-sizing: border-box; margin: 0; padding: 0; }
  html, body { width: 1194px; height: 1200px; overflow: hidden; background: var(--stage); }
  body { font-family: "Lato", Arial, sans-serif; color: var(--ink); position: relative; }

  .flyer { position: absolute; top: 47px; width: 526px; height: 1109px; background: var(--paper); overflow: hidden; box-shadow: 0 2px 8px rgba(0,0,0,.18); }
  .flyer--polo { left: 47px; }
  .flyer--knit { left: 620px; }
  .flyer > * { position: absolute; }

  .title-band { background: var(--green); color: var(--paper); font-weight: 900; text-transform: uppercase; letter-spacing: .5px; }
  .flyer--polo .title-band { left: 0; top: 27px; width: 526px; height: 42px; font-size: 31px; line-height: 42px; padding-left: 50px; }
  .flyer--knit .title-band { left: 0; top: 27px; width: 296px; height: 68px; font-size: 20px; line-height: 25px; padding: 9px 0 0 48px; }

  .brand { background: var(--paper); display: flex; flex-direction: column; justify-content: center; align-items: flex-start; padding-left: 14px; color: var(--ink-soft); font-weight: 400; line-height: 1; }
  .brand .brand-name { font-size: 40px; letter-spacing: -1px; }
  .brand .brand-line { font-size: 38px; letter-spacing: -.5px; }
  .flyer--polo .brand { left: 330px; top: 18px; width: 162px; height: 128px; }
  .flyer--knit .brand { left: 326px; top: 13px; width: 170px; height: 139px; }

  .intro { left: 38px; font-weight: 700; font-size: 18px; line-height: 23px; letter-spacing: .2px; white-space: nowrap; }
  .flyer--polo .intro { top: 165px; }
  .flyer--knit .intro { top: 237px; }

  .ticks { list-style: none; font-size: 18px; line-height: 30px; }
  .ticks li { display: flex; align-items: center; gap: 8px; }
  .ticks svg { width: 14px; height: 14px; flex: none; }
  .flyer--polo .ticks { left: 38px; top: 266px; }
  .flyer--knit .ticks { left: 38px; top: 317px; }

  .price-badge { left: 371px; top: 258px; width: 100px; height: 100px; border-radius: 50%; background: var(--green-light); text-align: center; padding-top: 15px; line-height: 1.05; font-weight: 700; }
  .price-badge .from { font-size: 18px; }
  .price-badge .amount { font-size: 21px; font-weight: 900; }
  .price-badge .tax { font-size: 11px; margin-top: 3px; }

  .media { display: block; }
  .color-range { left: 38px; top: 381px; width: 454px; height: 146px; }
  .family-photo { left: 237px; top: 591px; width: 289px; height: 419px; }
  .shelf-photo { left: 0; top: 0; width: 526px; height: 208px; }
  .sweater-photo { left: 299px; top: 379px; width: 227px; height: 220px; }

  .section h3 { color: var(--green); font-size: 21px; line-height: 26px; font-weight: 700; margin-bottom: 2px; }
  .section p { font-size: 17.5px; line-height: 24px; }
  .flyer--polo .section { left: 38px; }
  .sec-sizes { top: 568px; }
  .sec-embroidery { top: 692px; }
  .sec-stitchprice { top: 797px; width: 192px; }
  .sec-stitchprice p { line-height: 26.5px; }
  .sec-stitchprice .jl { display: block; text-align: justify; text-align-last: justify; white-space: nowrap; }
  .sec-stitchprice .jl.last { text-align-last: left; }

  .flyer--knit .section { left: 38px; width: 470px; }
  .knit-sizes { top: 459px; }
  .knit-embroidery { top: 560px; }
  .stock-note { left: 38px; top: 659px; font-weight: 700; font-size: 17px; line-height: 24px; white-space: nowrap; }
  .articles { left: 38px; top: 748px; font-size: 13px; line-height: 17.7px; white-space: nowrap; }
  .knit-price { top: 849px; }
  .knit-price p { font-weight: 700; }
  .knit-refs { top: 931px; }
  .knit-refs p { white-space: nowrap; line-height: 25.5px; }
  .knit-refs .clubs { font-size: 14px; line-height: 18.5px; margin-top: 3px; }

  .contact-band { left: 0; top: 1010px; width: 526px; height: 99px; background: var(--green); color: var(--paper); text-align: center; font-size: 14.5px; line-height: 17.7px; padding-top: 15px; }
  .contact-band strong { font-size: 15.5px; font-weight: 700; display: block; }
  .foot-band { left: 0; top: 1085px; width: 526px; height: 24px; background: var(--green); }
</style>
</head>
<body>

<article class="flyer flyer--polo">
  <div class="title-band">Poloshirts</div>
  <div class="brand"><span class="brand-name">velmax</span><span class="brand-line">artline</span></div>

  <p class="intro">Wir bieten Ihnen ein großes Sortiment an kurzfristig<br>verfügbaren POLO SHIRTS für Damen, Herren und<br>Kinder aus Baumwolle, Mischqualität oder Funktions-<br>Polyester an.</p>

  <ul class="ticks">
    <li><svg viewBox="0 0 14 14"><path d="M1.5 7.5 5.5 11.5 12.5 2.5" fill="none" stroke="#6cbb2e" stroke-width="2.4"/></svg>sehr große Farbauswahl</li>
    <li><svg viewBox="0 0 14 14"><path d="M1.5 7.5 5.5 11.5 12.5 2.5" fill="none" stroke="#6cbb2e" stroke-width="2.4"/></svg>Lieferzeit: ab Lager, kurzfristig</li>
    <li><svg viewBox="0 0 14 14"><path d="M1.5 7.5 5.5 11.5 12.5 2.5" fill="none" stroke="#6cbb2e" stroke-width="2.4"/></svg>sehr große Farbauswahl</li>
  </ul>

  <div class="price-badge"><div class="from">ab</div><div class="amount">€ 11,90</div><div class="tax">zzgl. MwSt.</div></div>

  <svg class="media color-range" role="img" aria-label="Farbpalette der Poloshirts: Reihen farbiger Shirts mit Farbbezeichnungen" viewBox="0 0 454 146" preserveAspectRatio="none">
    <defs><linearGradient id="polo-colors" x1="0" x2="1"><stop offset="0" stop-color="#d8332f"/><stop offset=".25" stop-color="#e8d84a"/><stop offset=".45" stop-color="#4daa3c"/><stop offset=".65" stop-color="#6a5aa8"/><stop offset=".85" stop-color="#3c8fc8"/><stop offset="1" stop-color="#3a3a3a"/></linearGradient></defs>
    <rect width="454" height="146" fill="url(#polo-colors)" opacity=".8"/>
  </svg>

  <section class="section sec-sizes"><h3>Größen</h3><p>Herren: S-3XL<br>Damen: XS-XXL<br>Kinder: 98-164</p></section>
  <section class="section sec-embroidery"><h3>Bestickung</h3><p>Veredelung möglich<br>Mindestmenge: 6 Stück</p></section>
  <section class="section sec-stitchprice"><h3>Stickpreis</h3><p>
    <span class="jl">Nach Vorlage Ihres</span>
    <span class="jl">gewünschten Stick-</span>
    <span class="jl">motives mit Größen-</span>
    <span class="jl">angabe unterbreiten</span>
    <span class="jl">wir Ihnen gerne ein</span>
    <span class="jl">individuelles Angebot</span>
    <span class="jl last">zum Stickpreis.</span>
  </p></section>

  <svg class="media family-photo" role="img" aria-label="Foto einer lachenden Familie in Poloshirts auf einem Golfrasen" viewBox="0 0 289 419" preserveAspectRatio="none">
    <defs><linearGradient id="family-tones" x1="0" y1="0" x2="0" y2="1"><stop offset="0" stop-color="#ffffff"/><stop offset=".35" stop-color="#d9b8a2"/><stop offset=".7" stop-color="#c9c7c4"/><stop offset="1" stop-color="#5f8f3a"/></linearGradient></defs>
    <rect width="289" height="419" fill="url(#family-tones)"/>
  </svg>

  <div class="contact-band">
    <strong>Velmax Handelsvertretung</strong>
    Korbacher Straße 14 · 34127 Bergfeld<br>
    Tel. + 49 561 5540231 · Fax +49 561 5540232<br>
    Mail: kontakt@velmax.de · Web: www.velmax.de
  </div>
</article>

<article class="flyer flyer--knit">
  <svg class="media shelf-photo" role="img" aria-label="Foto eines Regals mit gestapelten Pullovern in vielen Farben" viewBox="0 0 526 208" preserveAspectRatio="none">
    <defs><linearGradient id="shelf-tones" x1="0" x2="1"><stop offset="0" stop-color="#e9d24c"/><stop offset=".3" stop-color="#e78a3a"/><stop offset=".55" stop-color="#d9414a"/><stop offset=".8" stop-color="#4a6fb8"/><stop offset="1" stop-color="#5a4a6a"/></linearGradient></defs>
    <rect width="526" height="208" fill="url(#shelf-tones)" opacity=".85"/>
  </svg>
  <div class="title-band">Strickpullover/-<br>Pullunder</div>
  <div class="brand"><span class="brand-name">velmax</span><span class="brand-line">artline</span></div>

  <p class="intro">Wir bieten Ihnen Merino-Strickpullover und -Pullunder<br>für Damen und Herren in feinster Qualität - in verschie-<br>denen klassischen und modischen Farben.</p>

  <ul class="ticks">
    <li><svg viewBox="0 0 14 14"><path d="M1.5 7.5 5.5 11.5 12.5 2.5" fill="none" stroke="#6cbb2e" stroke-width="2.4"/></svg>100% australische Merinowolle</li>
    <li><svg viewBox="0 0 14 14"><path d="M1.5 7.5 5.5 11.5 12.5 2.5" fill="none" stroke="#6cbb2e" stroke-width="2.4"/></svg>bei 40 % maschinenwaschbar</li>
    <li><svg viewBox="0 0 14 14"><path d="M1.5 7.5 5.5 11.5 12.5 2.5" fill="none" stroke="#6cbb2e" stroke-width="2.4"/></svg>Total Easy Care Ausrüstung</li>
    <li><svg viewBox="0 0 14 14"><path d="M1.5 7.5 5.5 11.5 12.5 2.5" fill="none" stroke="#6cbb2e" stroke-width="2.4"/></svg>trocknergeeignet</li>
  </ul>

  <svg class="media sweater-photo" role="img" aria-label="Foto aufgefächerter Strickpullover in verschiedenen Farben" viewBox="0 0 227 220" preserveAspectRatio="none">
    <defs><linearGradient id="sweater-tones" x1="0" y1="0" x2="1" y2="1"><stop offset="0" stop-color="#2a3a5a"/><stop offset=".35" stop-color="#9bb08a"/><stop offset=".6" stop-color="#e0708a"/><stop offset=".85" stop-color="#a04aa0"/><stop offset="1" stop-color="#1f5a3e"/></linearGradient></defs>
    <rect width="227" height="220" fill="url(#sweater-tones)" opacity=".85"/>
  </svg>

  <section class="section knit-sizes"><h3>Größen</h3><p>Herren: 48-58<br>Damen: 36-48</p></section>
  <section class="section knit-embroidery"><h3>Bestickung</h3><p>Veredelung möglich<br>Mindestmenge: 6 Stück</p></section>

  <p class="stock-note">Klassische Farben während der Saison ab Lager (je nach<br>Saisonverlauf) solange der Vorrat reicht. Bei modischen<br>Farben empfehlen wir Vororder.</p>

  <p class="articles">Artikel 59939 velmax artline V-Pullunder Herren<br>Artikel 59940 velmax artline V-Pullover Herren<br>Artikel 81602 velmax artline V-Pullunder Damen<br>Artikel 81603 velmax artline V-Pullover Damen</p>

  <section class="section knit-price"><h3>Preis</h3><p>Gerne unterbreiten wir Ihnen ein individuelles Angebot!</p></section>
  <section class="section knit-refs"><h3>Referenzen</h3><p>Mit unseren Qualitäten sind wir seit nunmehr 15 Jah-<br>ren in zahlreichen Pro Shops vertreten.</p><p class="clubs">GC Talbrunn e.V., GC Wiesenau, GC Hollbach, GC Ebersfeld, GC<br>Kranzsee, u.v.m.</p></section>

  <div class="foot-band"></div>
</article>

</body>
</html>
```